Cleaning service website design

We need a new nice web design(logo will be the same) for a new cleaning service Company:

Informations about Company and logo you can take from flyers in attachments.

This is a cleaning service Company which have simple rules and we would like to show that(in checklist form) on website:

- What we do and that we're Cleaning Green

- Why us?

- How much(our pricing is simple)

Also we would like to communicate with clients by some nice/big pictures on website and the most important thing is our phone number and short/fast Freestimate.

Also there should be some space for description about our Company.

Generally all information on main page can be short: about us, about service(what we do), last reviews, tips (for example: Tip of the week) and other can be some introduction to subpage where will be more information.

There will be few subpages like: About us, About our service, Photos(Before and after), Reviews , Tips, FAQ, Contact, Looking for a Job? - most of them will be just text so you can project just one example.

```html
<!DOCTYPE html>
<html lang="en">
<head>
<meta charset="utf-8">
<title>Tidy Nest – Cleaning Service</title>
<link href="https://fonts.googleapis.com/css2?family=Open+Sans:wght@300;400;600;700&family=Merriweather:wght@700;900&display=swap" rel="stylesheet">
<style>
:root{
  --navy:#1b2b3d;
  --navy-deep:#142130;
  --blue:#2f7fc4;
  --green:#5cb34a;
  --green-dark:#4a9a3b;
  --grey-bg:#ececec;
  --grey-panel:#f3f3f3;
  --text:#555;
  --white:#fff;
}
*{margin:0;padding:0;box-sizing:border-box}
html,body{width:816px;height:1200px;overflow:hidden;background:#fff}
body{font-family:"Open Sans",Arial,sans-serif;color:var(--text);font-size:9px;line-height:1.5}
.page{width:816px;height:1200px;position:relative}

.topbar{height:22px;background:var(--navy);display:flex;align-items:center;justify-content:space-between;padding:0 34px;color:var(--white);font-size:9px;font-weight:600}
.topbar .phone{display:flex;align-items:center;gap:5px}
.topbar .social{display:flex;gap:5px}
.topbar .social span{width:11px;height:11px;border-radius:50%;background:#4a5d72;display:block}

.hero{height:373px;position:relative;overflow:hidden}
.hero-art{position:absolute;inset:0;background:linear-gradient(180deg,#ffffff 0%,#f2f8fd 25%,#cfe6f6 55%,#7fbfe9 80%,#3f93d2 100%)}
.brand{position:absolute;left:34px;top:10px;display:flex;align-items:center;gap:8px}
.brand .dot{width:34px;height:34px;border-radius:50%;background:var(--green)}
.brand .name{font-weight:700;font-size:17px;color:var(--green-dark)}
.nav{position:absolute;right:34px;top:22px;display:flex;gap:13px}
.nav a{color:var(--navy);text-decoration:none;font-size:9px;font-weight:600}
.nav a.active{color:var(--blue)}
.price-badge{position:absolute;right:48px;top:128px;width:92px;height:100px;background:var(--navy);color:var(--white);text-align:center;padding-top:18px;clip-path:polygon(0 0,100% 0,100% 82%,50% 100%,0 82%)}
.price-badge .amt{font-size:34px;font-weight:300;line-height:1}
.price-badge .amt sup{font-size:15px;vertical-align:top}
.price-badge .sub{font-size:9px;margin-top:4px}
.tagline{position:absolute;left:108px;top:250px;width:520px;height:32px;background:var(--blue);color:var(--white);font-family:"Merriweather",serif;font-weight:900;font-size:18px;line-height:32px;text-align:center;letter-spacing:.5px}

.callbar{height:40px;background:var(--green);display:flex;align-items:center;justify-content:space-between;padding:0 40px 0 250px;color:var(--white);font-family:"Merriweather",serif;font-weight:700;font-size:19px}
.callbar .num{display:flex;align-items:center;gap:8px;font-size:20px}

.intro{display:flex;padding:22px 34px 0;height:252px;gap:24px}
.about{flex:1}
.section-title{font-size:20px;font-weight:300;color:var(--navy);border-left:4px solid var(--green);padding-left:8px;line-height:1.1;margin-bottom:14px}
.section-title em{font-style:normal;color:var(--blue)}
.about p{font-size:9.5px;line-height:1.7;margin-bottom:10px}
.about p a{color:var(--blue);text-decoration:none}
.why{width:300px;background:var(--grey-panel);padding:14px 16px;height:212px}
.why ul{list-style:none}
.why li{font-size:9.5px;padding:3px 0 3px 12px;position:relative;border-bottom:1px solid #e2e2e2}
.why li::before{content:"";position:absolute;left:0;top:9px;width:5px;height:5px;background:var(--green);border-radius:50%}

.reviews{height:150px;background:var(--grey-bg);text-align:center;padding:16px 70px 0}
.reviews .quote{font-family:"Merriweather",serif;color:var(--green);font-size:30px;line-height:.6;height:14px}
.reviews h2{font-size:22px;font-weight:300;color:var(--navy);margin-bottom:10px}
.reviews p{font-size:8.5px;font-style:italic;line-height:1.6}
.reviews .by{margin-top:4px;font-size:8px}

.lower{display:flex;padding:14px 34px 0;height:210px;gap:34px}
.tip{width:240px;height:185px;background:var(--blue);color:var(--white)}
.tip h3{font-family:"Merriweather",serif;font-size:19px;text-align:center;padding:8px 0 6px}
.tip-photo{margin:0 14px;height:120px;background:linear-gradient(135deg,#f2e3cf,#d9c0a0 60%,#b08e6b)}
.tip .caption{text-align:center;font-size:8px;padding-top:5px}
.pricing{flex:1;padding-top:6px}
.price-row{font-size:10px;margin-bottom:2px}
.price-row b{font-size:22px;font-weight:300;color:var(--blue);margin-right:4px}
.pricing .note{font-size:8px;margin-top:4px}
.pricing .link{font-size:8px;color:var(--green);margin-top:2px}

.footer{position:absolute;left:0;right:0;bottom:0;height:111px;background:var(--navy-deep);color:#b9c3ce;display:flex;padding:10px 34px;gap:40px;font-size:7.5px}
.footer h4{color:var(--white);font-size:8px;font-weight:700;margin-bottom:3px}
.footer .links{width:230px;line-height:1.3}
.footer .news{width:240px}
.footer .news .field{height:16px;background:#fff;margin-top:6px;width:170px;display:inline-block}
.footer .news .btn{display:inline-block;height:16px;padding:0 8px;background:var(--green);color:#fff;line-height:16px;vertical-align:top;margin-top:6px}
.footer .social{display:flex;gap:5px}
.footer .social span{width:13px;height:13px;border-radius:50%;background:#3d5067;display:block}
.footer .copy{position:absolute;bottom:8px;left:0;right:0;text-align:center;font-size:7px}
.callbar.bottom{position:absolute;left:0;right:0;bottom:111px}
</style>
</head>
<body>
<div class="page">
  <div class="topbar">
    <div class="phone">
      <svg width="10" height="10" viewBox="0 0 24 24"><path fill="#fff" d="M6.6 10.8a15 15 0 0 0 6.6 6.6l2.2-2.2c.3-.3.7-.4 1-.2 1.1.4 2.3.6 3.6.6.6 0 1 .4 1 1V20c0 .6-.4 1-1 1A17 17 0 0 1 3 4c0-.6.4-1 1-1h3.5c.6 0 1 .4 1 1 0 1.3.2 2.5.6 3.6.1.3 0 .7-.2 1z"/></svg>
      555.014.2290
    </div>
    <div class="social"><span></span><span></span><span></span></div>
  </div>

  <header class="hero">
    <div class="hero-art" role="img" aria-label="Hero image: globe wrapped in splashing clean water"></div>
    <div class="brand"><span class="dot"></span><span class="name">Tidy Nest</span></div>
    <nav class="nav">
      <a class="active" href="#">Home</a><a href="#">About us</a><a href="#">About our Services</a><a href="#">Photos</a><a href="#">Reviews</a><a href="#">Tips</a><a href="#">Contact</a><a href="#">Looking for job</a>
    </nav>
    <div class="price-badge"><div class="amt"><sup>$</sup>79</div><div class="sub">as low as</div></div>
    <div class="tagline">AFFORDABLY MAKING YOUR LIFE SIMPLER</div>
  </header>

  <div class="callbar">
    <span>It's simple... call Today!</span>
    <span class="num">
      <svg width="16" height="16" viewBox="0 0 24 24"><path fill="#fff" d="M6.6 10.8a15 15 0 0 0 6.6 6.6l2.2-2.2c.3-.3.7-.4 1-.2 1.1.4 2.3.6 3.6.6.6 0 1 .4 1 1V20c0 .6-.4 1-1 1A17 17 0 0 1 3 4c0-.6.4-1 1-1h3.5c.6 0 1 .4 1 1 0 1.3.2 2.5.6 3.6.1.3 0 .7-.2 1z"/></svg>
      555.014.2290
    </span>
  </div>

  <section class="intro">
    <div class="about">
      <h2 class="section-title">About Us?</h2>
      <p>Have you ever wondered what it would be like if your life was simpler? We're here to <a href="#">help you get there</a> by taking over the chore of house cleaning. With our help you'll have more time to spend on the things that matter most to you.</p>
      <p><a href="#">With Tidy Nest</a> you not only get a professional service, but you get it at an affordable price. The owner makes it a point to be at each and every cleaning to ensure your needs are met.</p>
    </div>
    <div class="why">
      <h2 class="section-title">Why <em>Choose Us?</em></h2>
      <ul>
        <li>Owner/s Present at Every Cleaning</li>
        <li>Locally Owned &amp; Operated</li>
        <li>Reliable &amp; Affordable</li>
        <li>All Supplies Provided</li>
        <li>Green Cleaning</li>
        <li>Pet Friendly</li>
        <li>No Contracts</li>
      </ul>
    </div>
  </section>

  <section class="reviews">
    <div class="quote">&ldquo;</div>
    <h2>Clients Review</h2>
    <p>Our home has never looked this good. The team arrives on time, works quickly and leaves every room spotless and fresh. Pricing was clear from the first call and there were no surprises at all. I finally have my weekends back for family, friends and rest. Friendly, careful and honest people I trust in my home every week.</p>
    <div class="by">- Jane Doe</div>
  </section>

  <section class="lower">
    <div class="tip">
      <h3>Tip of the Week</h3>
      <div class="tip-photo" role="img" aria-label="Photo of a family relaxing together on a clean sofa at home"></div>
      <div class="caption">Keep a small basket of supplies in every room</div>
    </div>
    <div class="pricing">
      <h2 class="section-title">Pricing is <em>Simple</em></h2>
      <div class="price-row"><b>$79</b>for homes less than 1000 sq ft</div>
      <div class="price-row"><b>$89</b>for homes 1000-1800 sq ft</div>
      <div class="price-row"><b>$99</b>for homes 1800-2600 sq ft</div>
      <div class="note">*If your home is larger than 2600 sq ft please call for a quote</div>
      <div class="link">*View our full pricing</div>
    </div>
  </section>

  <div class="callbar bottom">
    <span>It's simple... call Today!</span>
    <span class="num">555.014.2290</span>
  </div>

  <footer class="footer">
    <div class="links">
      <h4>LINKS</h4>
      Home<br>About us<br>About our services<br>Photos<br>Reviews<br>Tips<br>Contact<br>Looking for job
    </div>
    <div class="news">
      <h4>NEWSLETTER SUBSCRIBE</h4>
      Keep up with our news
      <div><span class="field"></span><span class="btn">Subscribe</span></div>
    </div>
    <div>
      <h4>SOCIAL</h4>
      <div class="social"><span></span><span></span><span></span></div>
    </div>
    <div class="copy">© 2014 Tidy Nest. All rights reserved.</div>
  </footer>
</div>
</body>
</html>
```